Brisk Wire Services - Electrical

We need flyers for electrical services.
Areas of work include new builds, office fitouts, switchboard upgrades, installation of ceiling fans, powerpoint and downlight upgrades, home theatre and AV systems, all exterior and emergency work. Free quotes
We would like to see designs with the colour Red with a young and modern design. Licence No: 83146K must be included and call Leopold on 0418693027.

Colors
ec1f27

```html
<!DOCTYPE html>
<html lang="en">
<head>
<meta charset="utf-8">
<title>Brisk Wire Services – Electrical Flyer</title>
<link rel="stylesheet" href="https://fonts.googleapis.com/css2?family=Jost:wght@400;500;800&display=swap">
<style>
  :root {
    --stage: #f08c74;
    --red: #ec1f27;
    --ink: #141010;
    --ink-deep: #0b0909;
    --glow: #6a0f12;
    --white: #ffffff;
    --silver-light: #f4f4f4;
    --silver-dark: #9a9a9a;
  }
  * { margin: 0; padding: 0; box-sizing: border-box; }
  html, body {
    width: 1200px; height: 871px; overflow: hidden;
    background: var(--stage);
    font-family: "Jost", sans-serif;
  }
  .flyer {
    position: absolute; left: 310px; top: 25px;
    width: 580px; height: 820px;
    background: radial-gradient(circle at 62% 52%, var(--glow) 0%, #2a0a0b 38%, var(--ink) 70%, var(--ink-deep) 100%);
    overflow: hidden;
    box-shadow: 0 18px 40px rgba(90, 30, 20, 0.35);
  }
  .hero { position: absolute; left: 0; top: 0; width: 580px; height: 420px; }
  .brand {
    position: absolute; left: 40px; top: 428px; color: var(--white);
    line-height: 1;
  }
  .brand-strong { display: block; font-size: 50px; font-weight: 800; letter-spacing: 0.5px; }
  .brand-light { display: block; font-size: 44px; font-weight: 400; margin-top: 4px; }
  .services { position: absolute; left: 40px; top: 540px; color: var(--white); }
  .services-title { font-size: 28px; font-weight: 500; line-height: 32px; margin-bottom: 8px; }
  .services-list { list-style: none; }
  .services-list li {
    display: flex; align-items: center; gap: 10px;
    font-size: 14px; line-height: 20px;
  }
  .services-list svg { width: 10px; height: 10px; flex: none; }
  .job-photo {
    position: absolute; right: 30px; width: 205px; height: 125px;
    border: 5px solid #d8d8d8;
    box-shadow: 0 4px 10px rgba(0,0,0,0.5);
  }
  .job-photo.first { top: 420px; background: linear-gradient(135deg, #dfe3e6, #9aa6ae 55%, #2b6fb3); }
  .job-photo.second { top: 560px; background: linear-gradient(135deg, #f2f2f2, #c9c3b8 45%, #2f55a8); }
  .contact-band {
    position: absolute; left: 0; bottom: 0; width: 100%; height: 78px;
    background: var(--red); color: var(--white);
    display: flex; align-items: center; justify-content: center; gap: 16px;
  }
  .phone { display: flex; align-items: center; gap: 10px; font-size: 34px; font-weight: 500; letter-spacing: 1px; }
  .phone svg { width: 24px; height: 24px; }
  .divider { width: 2px; height: 40px; background: var(--white); }
  .licence { font-size: 25px; font-weight: 400; }
</style>
</head>
<body>
  <article class="flyer">
    <svg class="hero" viewBox="0 0 580 420">
      <defs>
        <linearGradient id="hero-tones" x1="0" y1="0" x2="0.55" y2="1">
          <stop offset="0" stop-color="#e8e4df"/>
          <stop offset="0.3" stop-color="#b9c2c9"/>
          <stop offset="0.5" stop-color="#7d8a94"/>
          <stop offset="0.68" stop-color="#c9a23a"/>
          <stop offset="0.8" stop-color="#d9b136"/>
          <stop offset="1" stop-color="#4c5a3c"/>
        </linearGradient>
        <linearGradient id="silver" x1="0" y1="0" x2="1" y2="0">
          <stop offset="0" stop-color="var(--silver-dark)"/>
          <stop offset="0.5" stop-color="var(--silver-light)"/>
          <stop offset="1" stop-color="var(--silver-dark)"/>
        </linearGradient>
      </defs>
      <path role="img" aria-label="Worker in yellow overalls holding an orange hard hat beside rows of solar panels"
            d="M0 0 H580 V280 C420 380 180 410 0 372 Z" fill="url(#hero-tones)"/>
      <path aria-hidden="true" d="M0 372 C180 410 420 380 580 280 V300 C430 394 190 420 0 386 Z" fill="url(#silver)"/>
    </svg>

    <h1 class="brand">
      <span class="brand-strong">Brisk Wire</span>
      <span class="brand-light">Services</span>
    </h1>

    <section class="services">
      <h2 class="services-title">Our services</h2>
      <ul class="services-list">
        <li><svg viewBox="0 0 10 10"><path d="M5 1a4 4 0 1 0 4 4H5z" fill="none" stroke="#fff" stroke-width="1.6"/></svg>New builds</li>
        <li><svg viewBox="0 0 10 10"><path d="M5 1a4 4 0 1 0 4 4H5z" fill="none" stroke="#fff" stroke-width="1.6"/></svg>Office fitouts</li>
        <li><svg viewBox="0 0 10 10"><path d="M5 1a4 4 0 1 0 4 4H5z" fill="none" stroke="#fff" stroke-width="1.6"/></svg>Switchboard upgrades</li>
        <li><svg viewBox="0 0 10 10"><path d="M5 1a4 4 0 1 0 4 4H5z" fill="none" stroke="#fff" stroke-width="1.6"/></svg>Installation of ceiling fans</li>
        <li><svg viewBox="0 0 10 10"><path d="M5 1a4 4 0 1 0 4 4H5z" fill="none" stroke="#fff" stroke-width="1.6"/></svg>Powerpoint and downlight upgrades</li>
        <li><svg viewBox="0 0 10 10"><path d="M5 1a4 4 0 1 0 4 4H5z" fill="none" stroke="#fff" stroke-width="1.6"/></svg>Home theatre and av systems</li>
        <li><svg viewBox="0 0 10 10"><path d="M5 1a4 4 0 1 0 4 4H5z" fill="none" stroke="#fff" stroke-width="1.6"/></svg>All exterior and emergency work</li>
      </ul>
    </section>

    <div class="job-photo first" role="img" aria-label="Electrician with safety glasses testing wiring at a panel"></div>
    <div class="job-photo second" role="img" aria-label="Electrician in white hard hat working on a switchboard"></div>

    <footer class="contact-band">
      <span class="phone">
        <svg viewBox="0 0 24 24" aria-hidden="true"><path d="M6.6 10.8a15 15 0 0 0 6.6 6.6l2.2-2.2c.3-.3.7-.4 1-.2 1.1.4 2.3.6 3.6.6.6 0 1 .4 1 1V20c0 .6-.4 1-1 1A17 17 0 0 1 3 4c0-.6.4-1 1-1h3.5c.6 0 1 .4 1 1 0 1.3.2 2.5.6 3.6.1.3 0 .7-.2 1z" fill="#fff"/></svg>
        0418693027
      </span>
      <span class="divider" aria-hidden="true"></span>
      <span class="licence">Licence No: 83146K</span>
    </footer>
  </article>
</body>
</html>
```